6.5x9" Postcard Project for Organic and Sustainably powered Lawn Care Service

Hello,

Looking for a 6.6"Hx9"W postcard for my first direct mail project.

We are a full service lawn care company providing organic lawn treatment programs and full service lawn maintenance with solar powered electric equipment (and sometimes propane/biodiesel equipment for larger lawns and spaces). We are brand new to Houston and are in the midst of our rollout. This will be our first structured marketing effort so we want something that will grab people's attention as well as really do a good job telling people what we're about!

I have some logos and designs from some other products from the other franchisees and was wanting something similar.

Some of our info and "catch phrases":

Site: www.BrightLeafYardWorksHouston.com

Phone Number: 832.571.4083

"The Neighborhood's Healthiest Lawn"

"Changing The Way America Mows The Lawn"

"Come Clean"

"Clean. Green. Organic."
If at all possible please include standard every day direct mail indicia as well.

Please let me know if there is anything else I can do to assist making the best product possible.

Thanks!

Martin

Target Market(s)

Organic and Environmentally Minded people needing lawn service.

Industry/Entity Type

Lawn Care

Requirements
Must have
• Logo, website, phone number, invitation for free estimate

```html
<!DOCTYPE html>
<html lang="en">
<head>
<meta charset="utf-8">
<title>BrightLeaf Yard Works – Direct Mail Postcard</title>
<link rel="stylesheet" href="https://fonts.googleapis.com/css2?family=Domine:wght@700&family=PT+Sans:wght@400;700&display=swap">
<style>
  :root {
    --leaf-green: #6fbe44;
    --deep-green: #4e9a2b;
    --sun-yellow: #ecb51f;
    --ink: #4a4340;
    --paper: #ffffff;
    --backdrop: #e9e7e4;
    --sky: #bfe0f4;
    --sky-light: #eef6fb;
    --grass: #7cbf3a;
    --grass-dark: #4f8f22;
  }
  * { box-sizing: border-box; margin: 0; padding: 0; }
  html, body { width: 1058px; height: 1200px; overflow: hidden; }
  body {
    background: var(--backdrop);
    position: relative;
    font-family: "PT Sans", sans-serif;
    color: var(--ink);
  }
  .postcard {
    position: absolute;
    width: 737px;
    height: 531px;
    background: var(--paper);
    box-shadow: 0 4px 14px rgba(0,0,0,.18);
    overflow: hidden;
  }
  .postcard--front { left: 121px; top: 43px; }
  .postcard--back { left: 209px; top: 618px; }
  .mail-stripe {
    position: absolute; left: 0; bottom: 0; width: 100%; height: 18px;
    background: var(--leaf-green);
  }

  /* Front */
  .hero-photo {
    position: absolute; left: 0; top: 0; width: 100%; height: 382px;
    background: linear-gradient(180deg, var(--sky) 0%, var(--sky-light) 45%, #d9ecc4 62%, var(--grass) 78%, var(--grass-dark) 100%);
  }
  .callout {
    position: absolute;
    background: var(--sun-yellow);
    border-radius: 24px;
    color: var(--paper);
    text-align: center;
  }
  .callout::before, .callout::after {
    content: ""; position: absolute; left: 50%;
    width: 18px; height: 18px; background: var(--sun-yellow);
    transform: translateX(-50%) rotate(45deg);
  }
  .callout::before { top: -8px; }
  .callout::after { bottom: -8px; }
  .callout--tagline {
    left: 81px; top: 89px; width: 305px; height: 98px;
    font-family: "Domine", serif; font-weight: 700;
    padding-top: 24px;
  }
  .callout--tagline .motto { font-size: 12.5px; letter-spacing: .2px; }
  .callout--tagline .slogan { font-size: 13.5px; margin-top: 9px; }
  .service-banner {
    position: absolute; left: 11px; top: 353px; width: 323px; height: 70px;
    background: var(--leaf-green);
    clip-path: polygon(0 0, 92% 0, 100% 100%, 0 100%);
    color: var(--paper);
    font-family: "Domine", serif; font-weight: 700;
    font-size: 15px; line-height: 19px;
    padding: 16px 0 0 15px;
  }
  .contact { position: absolute; left: 22px; top: 434px; }
  .contact .invite { font-size: 12.5px; }
  .contact .site { font-size: 14.5px; font-weight: 700; color: var(--deep-green); margin-top: 8px; letter-spacing: .2px; }
  .contact .phone { display: flex; align-items: center; gap: 8px; font-size: 14.5px; font-weight: 700; margin-top: 8px; }
  .brand {
    position: absolute; display: flex; align-items: center; gap: 10px;
    font-family: "Domine", serif; font-weight: 700; color: var(--leaf-green);
  }
  .brand-dot { border-radius: 50%; background: var(--leaf-green); flex: none; }
  .brand--front { left: 405px; top: 405px; font-size: 25px; }
  .brand--front .brand-dot { width: 26px; height: 26px; }

  /* Back */
  .brand--back { left: 30px; top: 54px; width: 125px; font-size: 14px; line-height: 18px; gap: 8px; }
  .brand--back .brand-dot { width: 16px; height: 16px; }
  .back-heading {
    position: absolute; left: 172px; top: 50px;
    font-family: "Domine", serif; font-weight: 700; font-size: 16px; line-height: 30px;
  }
  .back-heading .lead { color: var(--leaf-green); }
  .back-heading .values { color: var(--sun-yellow); }
  .indicia {
    position: absolute; left: 622px; top: 25px; width: 91px; height: 58px;
    border: 1.5px solid #222; color: #222;
    font-size: 8px; line-height: 10.5px; text-align: center; padding-top: 5px;
  }
  .indicia strong { font-size: 9.5px; }
  .benefits-panel {
    position: absolute; left: 0; top: 136px; width: 471px; height: 377px;
    background: linear-gradient(180deg, #d4e9f6 0%, var(--sky-light) 40%, #f3f8f6 65%, var(--grass) 84%, var(--grass-dark) 100%);
  }
  .benefits { position: absolute; left: 33px; top: 171px; width: 418px; list-style: none; }
  .benefits li { display: flex; gap: 8px; font-size: 13px; line-height: 18px; margin-bottom: 16px; }
  .benefits svg { flex: none; margin-top: 2px; }
  .callout--cta { left: 81px; top: 328px; width: 328px; height: 92px; padding-top: 9px; }
  .callout--cta .invite { font-size: 12.5px; }
  .callout--cta .site { font-size: 14.5px; font-weight: 700; margin-top: 6px; letter-spacing: .2px; }
  .callout--cta .phone { display: flex; justify-content: center; align-items: center; gap: 8px; font-size: 14.5px; font-weight: 700; margin-top: 8px; }
</style>
</head>
<body>

<section class="postcard postcard--front">
  <div class="hero-photo" role="img" aria-label="Photo of a toddler in a yellow hazmat suit and goggles standing in a green lawn in front of a house under a blue sky"></div>
  <div class="callout callout--tagline">
    <p class="motto">CLEAN. GREEN. ORGANIC</p>
    <p class="slogan">The Neighborhood's Healthiest Lawn</p>
  </div>
  <div class="service-banner">Organic and Sustainably powered<br>Lawn Care</div>
  <div class="contact">
    <p class="invite">Visit Our Website to Get a FREE ESTIMATE</p>
    <p class="site">www.BrightLeafYardWorksHouston.com</p>
    <p class="phone">
      <svg width="20" height="20" viewBox="0 0 20 20" aria-hidden="true"><circle cx="10" cy="10" r="8.5" fill="none" stroke="#4a4340" stroke-width="1.5"/><path d="M7 5.5l1.6 2.4-1 1.1c.6 1.3 1.6 2.3 2.9 2.9l1.1-1 2.4 1.6-.8 1.5c-3.6-.3-6.7-3.4-7-7z" fill="#4a4340"/></svg>
      832.571.4083
    </p>
  </div>
  <div class="brand brand--front"><span class="brand-dot"></span>BrightLeaf Yard Works</div>
  <div class="mail-stripe"></div>
</section>

<section class="postcard postcard--back">
  <div class="brand brand--back"><span class="brand-dot"></span><span>BrightLeaf<br>Yard Works</span></div>
  <h2 class="back-heading">
    <span class="lead">BRIGHTLEAF YARD WORKS IS:</span><br>
    <span class="values">CLEAN, ORGANIC, RENEWABLE</span>
  </h2>
  <div class="indicia">STD U.S. POSTAGE<br><strong>PAID</strong><br>PLACIDA, FL<br>PERMIT NO. 10</div>
  <div class="benefits-panel" role="img" aria-label="Photo of a soft blue sky over a fresh green lawn"></div>
  <ul class="benefits">
    <li><svg width="16" height="16" viewBox="0 0 16 16" aria-hidden="true"><circle cx="8" cy="8" r="8" fill="#6fbe44"/><path d="M6.5 4.5L10 8l-3.5 3.5" fill="none" stroke="#fff" stroke-width="1.8"/></svg>Organic treatment programs to ensure your lawn is beautiful and safe for children, pets, and our local environment.</li>
    <li><svg width="16" height="16" viewBox="0 0 16 16" aria-hidden="true"><circle cx="8" cy="8" r="8" fill="#6fbe44"/><path d="M6.5 4.5L10 8l-3.5 3.5" fill="none" stroke="#fff" stroke-width="1.8"/></svg>Clean and quiet electric equipment powered by renewable resources</li>
    <li><svg width="16" height="16" viewBox="0 0 16 16" aria-hidden="true"><circle cx="8" cy="8" r="8" fill="#6fbe44"/><path d="M6.5 4.5L10 8l-3.5 3.5" fill="none" stroke="#fff" stroke-width="1.8"/></svg>Lawn care practices that maximize water conservation and nutrient uptake</li>
  </ul>
  <div class="callout callout--cta">
    <p class="invite">Visit Our Website to Get a FREE ESTIMATE</p>
    <p class="site">www.BrightLeafYardWorksHouston.com</p>
    <p class="phone">
      <svg width="20" height="20" viewBox="0 0 20 20" aria-hidden="true"><circle cx="10" cy="10" r="8.5" fill="none" stroke="#fff" stroke-width="1.5"/><path d="M7 5.5l1.6 2.4-1 1.1c.6 1.3 1.6 2.3 2.9 2.9l1.1-1 2.4 1.6-.8 1.5c-3.6-.3-6.7-3.4-7-7z" fill="#fff"/></svg>
      832.571.4083
    </p>
  </div>
  <div class="mail-stripe"></div>
</section>

</body>
</html>
```